Natural Immune System Booster

We need a pharmaceutical type box and label design for a vitamin supplement product. Korvelix is in process of being trademarked and should therefore carry the TM symbol. It is comprised of a special blend of over 20 vitamins, herbs and minerals with a High strength vitamin C booster. The tag line should read. The No.1 Natural Support For Your Immune System. Each tube contains 10 tablets. A bar code will be placed on the box carton. We prefer bright and vivid colours, preferably a mix of electric purple, yellow and orange mix. We have three flavours, summer berry (strawberry), tropical fruit and juicy orange - the box and label should indicate the flavours in a creative design element. Effervescent tabelts should be clearly marked on the box and label. The ingredients and instructions should be present on the box outer carton and also the label. We require an eye catching yet simple and bright design that pops off the shelf.
Updates

Target Market(s)

Target customers are male and female 20 - 60+ that live in Western countries that handle household budgets.

Industry/Entity Type

Pharmaceutical

Requirements
Must have
• Please see current box design, all necessary elements and specifications are included here. We require same to be placed on new design.

I have attached a txt file of the supplement facts and other details that are required for both the label and the box

```html
<!DOCTYPE html>
<html lang="en">
<head>
<meta charset="utf-8">
<title>Korvelix Effervescent Tablets – Carton Dieline</title>
<link rel="stylesheet" href="https://fonts.googleapis.com/css2?family=Open+Sans:ital,wght@0,400;0,700;0,800;1,400;1,700;1,800&display=swap">
<style>
  :root {
    --stage: #ecebee;
    --purple: #6b2d80;
    --purple-deep: #4a1a5c;
    --purple-light: #8a4aa0;
    --teal: #1d5b78;
    --yellow: #f8e71c;
    --orange: #f6a21e;
    --orange-soft: #ffc43a;
    --ribbon: #f29318;
    --paper: #ffffff;
    --ink: #1a1a1a;
    --cut: #2a2a2a;
    --type: "Open Sans", Arial, sans-serif;
  }
  html, body {
    margin: 0;
    width: 1200px;
    height: 1000px;
    overflow: hidden;
    background: var(--stage);
  }
  .dieline { display: block; width: 1200px; height: 1000px; }
  text { font-family: var(--type); }
  .cut { stroke: var(--cut); stroke-width: 0.7; }
  .flap { fill: var(--paper); }
  .panel-purple { fill: var(--purple); }
  .band-teal { fill: var(--teal); }
  .band-rule { stroke: var(--yellow); stroke-width: 1; }
  .band-copy { fill: #fff; font-weight: 700; font-style: italic; font-size: 11.5px; }
  .brand-name { fill: var(--yellow); font-weight: 800; font-size: 40px; }
  .brand-side { fill: var(--yellow); font-weight: 800; font-size: 27px; }
  .side-band-copy { fill: #fff; font-weight: 700; font-style: italic; font-size: 11px; }
  .tagline { fill: #fff; font-style: italic; font-size: 8.6px; }
  .ribbon-copy { fill: var(--purple-deep); font-weight: 800; font-style: italic; font-size: 11.5px; }
  .count-copy { fill: var(--yellow); font-weight: 800; font-size: 11px; }
  .flavour-copy { fill: var(--purple-deep); font-weight: 800; font-size: 11px; }
  .claim { fill: #fff; font-weight: 700; font-style: italic; font-size: 10.5px; }
  .chip { fill: var(--teal); stroke: var(--yellow); stroke-width: 0.8; }
  .chip-copy { fill: #fff; font-weight: 700; font-size: 8px; }
  .disclaimer-box { fill: none; stroke: #fff; stroke-width: 0.8; }
  .disclaimer { fill: #fff; font-size: 5.6px; }
  .dose-badge { fill: var(--teal); stroke: var(--yellow); stroke-width: 0.8; }
  .dose-copy { fill: var(--yellow); font-weight: 800; font-style: italic; font-size: 7.5px; }
  .lot-copy { fill: #fff; font-style: italic; font-size: 6.5px; }
  .lot-window { fill: #fff; }
  .facts-title { fill: var(--ink); font-weight: 800; font-size: 8.5px; }
  .facts { fill: var(--ink); font-size: 4.4px; }
  .facts-bold { fill: var(--ink); font-weight: 700; font-size: 4.6px; }
  .facts-rule { stroke: var(--ink); stroke-width: 0.5; }
  .facts-rule-heavy { stroke: var(--ink); stroke-width: 1.6; }
</style>
</head>
<body>
<svg class="dieline" viewBox="200 20 816 680" xmlns="http://www.w3.org/2000/svg" aria-label="Korvelix effervescent tablet carton, flat dieline">
  <defs>
    <radialGradient id="bubble-glow" cx="0.22" cy="0.45" r="0.6">
      <stop offset="0" stop-color="#8d4fa3"/>
      <stop offset="1" stop-color="#6b2d80"/>
    </radialGradient>

    <!-- Front face artwork, 400 x 140 -->
    <g id="front-face">
      <rect class="panel-purple" x="0" y="0" width="400" height="140"/>
      <rect x="0" y="20" width="400" height="120" fill="url(#bubble-glow)" role="img" aria-label="Soft purple bubble pattern"/>
      <rect class="band-teal" x="0" y="0" width="400" height="20"/>
      <line class="band-rule" x1="0" y1="20.5" x2="400" y2="20.5"/>
      <text class="band-copy" x="200" y="14.5" text-anchor="middle">Boost of Vitamin C with over 20 Herbs, Minerals and Vitamins</text>
      <path d="M0,100 C120,78 260,90 400,58 L400,72 C260,100 120,88 0,112 Z" fill="var(--orange-soft)"/>
      <path d="M0,110 C120,88 260,100 400,70 L400,140 L0,140 Z" fill="var(--orange)"/>
      <ellipse cx="300" cy="62" rx="13" ry="8" fill="var(--orange)" role="img" aria-label="Orange effervescent tablet"/>
      <text class="brand-name" x="206" y="72" text-anchor="middle">Korvelix</text>
      <text class="tagline" x="206" y="88" text-anchor="middle">The No. 1 Natural Support For Your Immune System*</text>
      <g transform="rotate(-4 226 104)">
        <polygon points="138,95 316,95 308,104 316,113 138,113 146,104" fill="var(--ribbon)"/>
        <text class="ribbon-copy" x="227" y="108.5" text-anchor="middle">EFFERVESCENT TABLETS</text>
      </g>
      <text class="count-copy" x="14" y="119">10</text>
      <text class="count-copy" x="14" y="133">TABLETS</text>
      <text class="flavour-copy" x="396" y="119" text-anchor="end">JUICY</text>
      <text class="flavour-copy" x="396" y="133" text-anchor="end">ORANGE</text>
    </g>
  </defs>

  <!-- Glue and tuck flaps -->
  <polygon class="flap cut" points="340,52 400,40 400,165 340,153"/>
  <polygon class="flap cut" points="790,40 850,52 850,153 790,165"/>
  <polygon class="flap cut" points="790,185 850,197 850,313 790,325"/>
  <polygon class="flap cut" points="340,342 390,330 390,470 340,458"/>
  <polygon class="flap cut" points="400,610 790,610 790,660 770,680 420,680 400,660"/>

  <!-- Top closure panel -->
  <g class="top-panel">
    <rect class="panel-purple cut" x="400" y="40" width="390" height="125"/>
    <text class="claim" x="425" y="75">Created by an Engineer and designed to be The</text>
    <text class="claim" x="425" y="89">No. 1 Natural Support For Your Immune System*</text>
    <rect class="chip" x="425" y="100" width="76" height="17"/>
    <text class="chip-copy" x="463" y="111.5" text-anchor="middle">10 TABLETS</text>
    <rect class="chip" x="510" y="100" width="162" height="17"/>
    <text class="chip-copy" x="591" y="111.5" text-anchor="middle">REPLACE CAP AFTER OPENING</text>
    <rect class="disclaimer-box" x="425" y="135" width="250" height="23"/>
    <text class="disclaimer" x="550" y="144.5" text-anchor="middle">*This statement has not been evaluated by the US Food and Drug Administration.</text>
    <text class="disclaimer" x="550" y="152.5" text-anchor="middle">This product is not intended to diagnose, treat, cure or prevent any disease.</text>
    <ellipse class="dose-badge" cx="735" cy="69" rx="38" ry="22"/>
    <text class="dose-copy" x="735" y="62" text-anchor="middle">TAKE</text>
    <text class="dose-copy" x="735" y="71" text-anchor="middle">UPTO 3 TIMES</text>
    <text class="dose-copy" x="735" y="80" text-anchor="middle">PER DAY</text>
    <text class="lot-copy" x="700" y="110">LOT NO:</text>
    <text class="lot-copy" x="700" y="119">EXP DATE:</text>
    <rect class="lot-window" x="693" y="128" width="80" height="36" rx="6"/>
  </g>

  <!-- Left end panel -->
  <g class="end-panel">
    <polygon class="panel-purple cut" points="245,197 400,185 400,325 245,313"/>
    <rect x="245" y="185" width="155" height="140" fill="url(#bubble-glow)" opacity="0.6" role="img" aria-label="Soft purple bubble pattern"/>
    <g transform="translate(400,185) rotate(90)">
      <rect class="band-teal" x="0" y="124" width="140" height="20"/>
      <line class="band-rule" x1="0" y1="123.5" x2="140" y2="123.5"/>
      <line class="band-rule" x1="0" y1="144.5" x2="140" y2="144.5"/>
      <text class="brand-side" x="70" y="116" text-anchor="middle">Korvelix</text>
      <text class="side-band-copy" x="70" y="138" text-anchor="middle">Effervescent Tablets</text>
    </g>
  </g>

  <!-- Supplement facts panel -->
  <g class="facts-panel">
    <rect class="flap cut" x="400" y="185" width="390" height="140"/>
    <g transform="translate(414,318) rotate(-90)">
      <text class="facts-title" x="2" y="9">SUPPLEMENT FACTS</text>
      <line class="facts-rule" x1="2" y1="12" x2="126" y2="12"/>
      <text class="facts" x="2" y="18">Serving size: 1 Tablet</text>
      <line class="facts-rule-heavy" x1="2" y1="21" x2="126" y2="21"/>
      <text class="facts" x="2" y="27">Each Serving Contains</text>
      <text class="facts" x="96" y="27" text-anchor="end">Amount Per Serving</text>
      <text class="facts" x="126" y="27" text-anchor="end">%DV</text>
      <line class="facts-rule" x1="2" y1="30" x2="126" y2="30"/>
      <g class="facts-rows">
        <text class="facts" x="2" y="36">Calories</text><text class="facts" x="96" y="36" text-anchor="end">5</text><text class="facts" x="126" y="36" text-anchor="end"></text>
        <text class="facts" x="2" y="44">Vitamin A (As Retinyl Acetate)</text><text class="facts" x="96" y="44" text-anchor="end">2100IU</text><text class="facts" x="126" y="44" text-anchor="end">41%</text>
        <text class="facts" x="2" y="52">Vitamin C (As Ascorbic Acid)</text><text class="facts" x="96" y="52" text-anchor="end">1000mg</text><text class="facts" x="126" y="52" text-anchor="end">1670%</text>
        <text class="facts" x="2" y="60">Vitamin E (As Tocopheryl Acetate)</text><text class="facts" x="96" y="60" text-anchor="end">30IU</text><text class="facts" x="126" y="60" text-anchor="end">100%</text>
        <text class="facts" x="2" y="68">Riboflavin (As Vitamin B2)</text><text class="facts" x="96" y="68" text-anchor="end">1.7mg</text><text class="facts" x="126" y="68" text-anchor="end">100%</text>
        <text class="facts" x="2" y="76">Magnesium (As Oxide)</text><text class="facts" x="96" y="76" text-anchor="end">40mg</text><text class="facts" x="126" y="76" text-anchor="end">10%</text>
        <text class="facts" x="2" y="84">Zinc (As Sulphate)</text><text class="facts" x="96" y="84" text-anchor="end">10mg</text><text class="facts" x="126" y="84" text-anchor="end">65%</text>
        <text class="facts" x="2" y="92">Selenium (As Yeast)</text><text class="facts" x="96" y="92" text-anchor="end">15µg</text><text class="facts" x="126" y="92" text-anchor="end">22%</text>
        <text class="facts" x="2" y="100">Manganese (As Sulphate)</text><text class="facts" x="96" y="100" text-anchor="end">5mg</text><text class="facts" x="126" y="100" text-anchor="end">250%</text>
        <text class="facts" x="2" y="108">Sodium (As Bicarbonate)</text><text class="facts" x="96" y="108" text-anchor="end">230mg</text><text class="facts" x="126" y="108" text-anchor="end">9.5%</text>
        <text class="facts" x="2" y="116">Potassium (As Bicarbonate)</text><text class="facts" x="96" y="116" text-anchor="end">75mg</text><text class="facts" x="126" y="116" text-anchor="end">2%</text>
      </g>
      <line class="facts-rule-heavy" x1="2" y1="121" x2="126" y2="121"/>
      <text class="facts-bold" x="2" y="130">PROPRIETARY HERBAL BLEND (400mg*)</text>
      <text class="facts" x="2" y="137">Echinacea, Ginger Root, Elderberry, Olive Leaf,</text>
      <text class="facts" x="2" y="143">Garlic, Turmeric, Green Tea, Rosehip, Nettle,</text>
      <text class="facts" x="2" y="149">Licorice Root, Astragalus, Peppermint Leaf</text>
      <text class="facts-bold" x="2" y="158">PROPRIETARY AMINO ACID BLEND (5mg*)</text>
      <text class="facts" x="2" y="165">L-Lysine, L-Glutamine</text>
      <line class="facts-rule-heavy" x1="2" y1="170" x2="126" y2="170"/>
      <text class="facts" x="2" y="180">*Daily value not established. Percent Daily Values are</text>
      <text class="facts" x="2" y="186">based on a 2,000 calorie diet. Other ingredients: Citric</text>
      <text class="facts" x="2" y="192">Acid, Sodium Bicarbonate, Sorbitol, Natural Flavour.</text>
      <text class="facts" x="2" y="204"><tspan font-weight="700">Directions:</tspan> For adults and children 12 years and older.</text>
      <text class="facts" x="2" y="210">Dissolve one tablet in 8 fl oz of water. Take up</text>
      <text class="facts" x="2" y="216">to 3 times per day. Do not exceed stated dose.</text>
      <text class="facts" x="2" y="222">Consult your doctor if pregnant or nursing.</text>
      <text class="facts" x="2" y="234"><tspan font-weight="700">Distributed By:</tspan> Korvelix LLC, 1200 Harbor Lane,</text>
      <text class="facts" x="2" y="240">Fairview, ST 00000</text>
      <text class="facts" x="2" y="246"><tspan font-weight="700">Questions?</tspan> Email: care@korvelix.example</text>
      <text class="facts" x="2" y="252">Web: korvelix.example  Tel: 1-800-555-0142</text>
    </g>
  </g>

  <!-- Front faces -->
  <use href="#front-face" transform="translate(390,330)"/>
  <rect class="cut" x="390" y="330" width="400" height="140" fill="none"/>
  <use href="#front-face" transform="translate(395,472) scale(0.9875,0.985)"/>
  <rect class="cut" x="395" y="472" width="395" height="138" fill="none"/>

  <!-- Right end panel -->
  <g class="end-panel">
    <polygon class="panel-purple cut" points="790,330 935,342 935,458 790,470"/>
    <rect x="790" y="330" width="145" height="140" fill="url(#bubble-glow)" opacity="0.6" role="img" aria-label="Soft purple bubble pattern"/>
    <g transform="translate(790,470) rotate(-90)">
      <rect class="band-teal" x="0" y="104" width="140" height="20"/>
      <line class="band-rule" x1="0" y1="103.5" x2="140" y2="103.5"/>
      <line class="band-rule" x1="0" y1="124.5" x2="140" y2="124.5"/>
      <text class="brand-side" x="70" y="96" text-anchor="middle">Korvelix</text>
      <text class="side-band-copy" x="70" y="118" text-anchor="middle">Effervescent Tablets</text>
    </g>
  </g>
</svg>
</body>
</html>
```